Business card design needed

Our company background is that we provides transfers to and from the airport, social & corporate events, weddings.
We are also available for charter for birthday party, wine tastings, concerts, anniversary, school balls etc.
Our business cards have to reflect that we have a professional company, they are our first contact and have to stand out from the other 'players' in the market.

Industry/Entity Type

School

Contact Information for Business Card

VESTAR PTH, Teodor & Marguerite, mob: 0427 381 592, PO Box 284, Larkmoor WA 6871, ABN 52 614 203 178, Lic 7169/2058,

Requirements
Must have
• Telephone number: 0427 381 592
Website: www.VESTARPTH.com.au
postal address: PO Box 284, Larkmoor WA 6871
Licences: Lic 7169/2058

***If using the new photo (one with the bus and buildings behind it), if possible can the buildings be cropped out. Thanks
Nice to have
• would be nice to have the pics of the vehicle(s), preferred the Vel on the card but not too fussed.
Should not have
• Picture of vehicle we don't have in our fleet. (We ONLY have the Velarions and Murako Densa mini bus)

```html
<!DOCTYPE html>
<html lang="en">
<head>
<meta charset="utf-8">
<title>Vestar PTH – Business Card</title>
<link rel="stylesheet" href="https://fonts.googleapis.com/css2?family=Raleway:wght@300;400&family=Cormorant+SC:wght@500&display=swap">
<style>
  :root {
    --page: #e6e9ec;
    --blue-deep: #0b5f95;
    --blue-mid: #1c8cc6;
    --blue-light: #4cb6e4;
    --ink: #ffffff;
    --ink-soft: rgba(255,255,255,0.82);
    --stripe: rgba(255,255,255,0.05);
    --van-light: #f4f6f8;
    --van-shade: #a9b2bb;
    --car-light: #6d737a;
    --car-dark: #16191d;
  }
  * { box-sizing: border-box; margin: 0; padding: 0; }
  html, body { width: 1200px; height: 801px; overflow: hidden; }
  body {
    background: var(--page);
    display: flex; align-items: center; justify-content: center;
    font-family: "Raleway", sans-serif;
  }
  .business-card {
    position: relative;
    width: 1080px; height: 660px;
    border-radius: 6px;
    overflow: hidden;
    color: var(--ink);
    background:
      repeating-linear-gradient(45deg, var(--stripe) 0 2px, transparent 2px 7px),
      radial-gradient(ellipse at 30% 40%, var(--blue-light) 0%, var(--blue-mid) 45%, var(--blue-deep) 100%);
    box-shadow: 0 10px 30px rgba(0,0,0,0.18);
  }
  .brand {
    position: absolute; left: 80px; top: 70px;
    text-align: center; width: 440px;
  }
  .brand-name {
    font-family: "Raleway", sans-serif;
    font-weight: 300;
    font-size: 104px;
    line-height: 1;
    color: var(--ink);
  }
  .brand-tagline {
    font-family: "Cormorant SC", serif;
    font-weight: 500;
    font-size: 38px;
    letter-spacing: 1px;
    color: var(--ink);
    margin-top: 12px;
  }
  .contact {
    position: absolute; left: 80px; top: 355px;
  }
  .contact-company {
    font-size: 42px; font-weight: 400; letter-spacing: 1px;
  }
  .contact-people {
    font-size: 26px; font-weight: 300; color: var(--ink-soft);
    margin: 4px 0 26px;
  }
  .contact-list { list-style: none; }
  .contact-item {
    display: flex; align-items: center; gap: 16px;
    font-size: 24px; font-weight: 300;
    line-height: 1; margin-bottom: 14px;
  }
  .contact-icon { width: 24px; height: 24px; flex: none; }
  .vehicle {
    position: absolute;
    border-radius: 40px 60px 18px 18px;
  }
  .vehicle-van {
    right: 70px; top: 70px; width: 430px; height: 250px;
    background: linear-gradient(160deg, var(--van-light) 0%, #dde2e7 55%, var(--van-shade) 100%);
    box-shadow: 0 18px 22px -14px rgba(0,0,0,0.45);
  }
  .vehicle-car {
    right: 80px; top: 395px; width: 420px; height: 190px;
    border-radius: 70px 90px 24px 24px;
    background: linear-gradient(160deg, var(--car-light) 0%, #2c3036 50%, var(--car-dark) 100%);
    box-shadow: 0 18px 22px -14px rgba(0,0,0,0.5);
  }
</style>
</head>
<body>
  <article class="business-card">
    <header class="brand">
      <div class="brand-name">Vestar</div>
      <div class="brand-tagline">Luxury Car &amp; Coach</div>
    </header>

    <section class="contact">
      <h1 class="contact-company">VESTAR PTH</h1>
      <p class="contact-people">Teodor &amp; Marguerite</p>
      <ul class="contact-list">
        <li class="contact-item">
          <svg class="contact-icon" viewBox="0 0 24 24" fill="none" stroke="currentColor" stroke-width="1.6"><path d="M6 3h3l2 5-2.5 1.5a11 11 0 0 0 6 6L16 13l5 2v3a2 2 0 0 1-2 2A16 16 0 0 1 4 5a2 2 0 0 1 2-2z"/></svg>
          <span>0427 381 592</span>
        </li>
        <li class="contact-item">
          <svg class="contact-icon" viewBox="0 0 24 24" fill="none" stroke="currentColor" stroke-width="1.6"><rect x="3" y="6" width="18" height="13" rx="1.5"/><path d="M3 7l9 6 9-6"/></svg>
          <span>PO Box 284, Larkmoor WA 6871</span>
        </li>
        <li class="contact-item">
          <svg class="contact-icon" viewBox="0 0 24 24" fill="none" stroke="currentColor" stroke-width="1.6"><circle cx="12" cy="12" r="9"/><path d="M3 12h18M12 3c3 3 3 15 0 18M12 3c-3 3-3 15 0 18"/></svg>
          <span>www.VESTARPTH.com.au</span>
        </li>
        <li class="contact-item">
          <svg class="contact-icon" viewBox="0 0 24 24" fill="none" stroke="currentColor" stroke-width="1.6"><rect x="5" y="3" width="14" height="18" rx="1.5"/><path d="M8 8h8M8 12h8M8 16h5"/></svg>
          <span>Lic 7169/2058</span>
        </li>
      </ul>
    </section>

    <div class="vehicle vehicle-van" role="img" aria-label="Photo of the white Murako Densa mini bus"></div>
    <div class="vehicle vehicle-car" role="img" aria-label="Photo of a black Velarions luxury sedan"></div>
  </article>
</body>
</html>
```